Web Design for a recruitment company

Website is for a recruitment company, with a particular focus on temporary staff, trades, skilled, and unskilled labour markets. Website will consist of a home page design and separate design for additional pages. Website will be implemented as a template in SharePoint. There is a separate design project for a new logo and look colours will need to be co-ordinated.

Target Market(s)

Company executives in the construction and trades areas looking for staff. Trades people, skilled and unskilled labourers looking for work.

Industry/Entity Type

It Company

Number of Pages Required

2 page

Requirements
Must have
• Looking for Home Page design plus design for additional pages.
• .
Nice to have
• Right People | Right Place is the firms byline, company name is Voskin Staffing. They will be in the Logo (separate project) but may also appear elsewhere in the design.
• Company values (attached file) may be reflected in the design where practical.

```html
<!DOCTYPE html>
<html lang="en">
<head>
<meta charset="utf-8">
<title>Voskin Staffing — Home</title>
<link href="https://fonts.googleapis.com/css2?family=Raleway:wght@400;500;600;700&display=swap" rel="stylesheet">
<style>
:root{
  --red:#c8281e;
  --ink:#222;
  --text:#3a3a3a;
  --muted:#777;
  --band:#2c2c2c;
  --card-head:#f6f6f6;
  --card-icon:#e4e4e4;
  --footer:#ececec;
  --footer-base:#f7f7f7;
  --line:#e6e6e6;
  --hero-a:#eceeef;
  --hero-b:#b9bcc0;
}
*{margin:0;padding:0;box-sizing:border-box}
html,body{width:792px;height:1200px;overflow:hidden;background:#fff}
body{font-family:'Raleway',sans-serif;color:var(--text);position:relative}
a{color:inherit;text-decoration:none}

.site-header{position:absolute;left:0;top:0;width:792px;height:75px}
.account-links{position:absolute;right:57px;top:8px;font-size:9px;color:var(--muted);word-spacing:4px}
.brand{position:absolute;font-size:19px;font-weight:700;color:var(--ink);line-height:1;white-space:nowrap}
.site-header .brand{left:54px;top:34px}
.main-nav{position:absolute;right:57px;top:34px;display:flex;gap:17px;font-size:9.5px;font-weight:500;color:var(--ink)}
.main-nav .active{color:var(--red);border-bottom:1.5px solid var(--red);padding-bottom:6px}

.hero{position:absolute;left:0;top:75px;width:792px;height:460px;background:linear-gradient(180deg,var(--hero-a) 0%,#d4d6d8 60%,var(--hero-b) 100%)}
.slider-dots{position:absolute;left:656px;top:531px;display:flex;gap:4px}
.slider-dots span{width:9px;height:8px;background:#777}
.slider-dots .on{background:var(--red)}

.values-band{position:absolute;left:0;top:535px;width:792px;height:69px;background:var(--band);color:#fff}
.values-band .arrow{position:absolute;top:27px;width:19px;height:18px;background:#3f3f3f;display:flex;align-items:center;justify-content:center}
.values-band .prev{left:17px}.values-band .next{right:17px}
.values-title{position:absolute;left:54px;top:24px;font-size:17px;font-weight:700;letter-spacing:.2px}
.value-name{position:absolute;left:303px;top:8px;font-size:25px;font-weight:400}
.value-line{position:absolute;left:303px;top:40px;font-size:13.5px;font-weight:400}

.section-title{position:absolute;left:0;width:792px;text-align:center;font-size:23px;font-weight:400;color:var(--red)}
.about-title{top:635px}
.about-text{position:absolute;left:70px;top:670px;width:652px;text-align:center;font-size:8.2px;line-height:14px}
.btn-outline{position:absolute;left:366px;top:725px;width:57px;height:17px;border:1px solid #bbb;font-size:8.4px;color:var(--red);display:flex;align-items:center;justify-content:center}

.service{position:absolute;top:776px;width:135px;height:157px;border-bottom:1px solid var(--line);text-align:center}
.service h3{height:36px;background:var(--card-head);font-size:8.8px;font-weight:600;color:var(--ink);padding-top:8px;line-height:11.5px;text-transform:uppercase}
.service .icon{height:54px;background:var(--card-icon);display:flex;align-items:center;justify-content:center}
.service p{font-size:8.4px;line-height:14px;padding:12px 14px 0}

.clients-title{top:965px}
.testimonial-photo{position:absolute;left:104px;top:996px;width:80px;height:80px;border-radius:50%;border:1px solid #ccc;background:radial-gradient(circle at 50% 45%,#d9b8a4 0%,#9a7563 45%,#e8e8e8 75%)}
.testimonial-text{position:absolute;left:207px;top:1005px;width:480px;font-size:8.3px;line-height:14px}

.site-footer{position:absolute;left:0;top:1118px;width:792px;height:56px;background:var(--footer);border-top:1px solid #d8d8d8}
.site-footer .brand{left:54px;top:18px}
.footer-nav{position:absolute;left:223px;top:22px;display:flex;gap:15px;font-size:8.6px;font-weight:500;color:var(--ink)}
.footer-nav .active{color:var(--red)}
.footer-base{position:absolute;left:0;top:1174px;width:792px;height:26px;background:var(--footer-base)}
.copyright{position:absolute;left:54px;top:8px;font-size:7.6px;color:var(--muted)}
.social{position:absolute;right:56px;top:4px;display:flex;gap:4px}
.social span{width:18px;height:18px;border-radius:50%}
</style>
</head>
<body>

<header class="site-header">
  <div class="account-links"><a href="#">Register</a> <a href="#">Login</a></div>
  <a class="brand" href="#">Voskin Staffing</a>
  <nav class="main-nav">
    <a class="active" href="#">Home</a><a href="#">Our Mission &amp; Vission</a><a href="#">Our Services</a><a href="#">About Us</a><a href="#">Contact Us</a>
  </nav>
</header>

<div class="hero" role="img" aria-label="Four job candidates in business attire seated on chairs holding résumés"></div>
<div class="slider-dots"><span class="on"></span><span></span><span></span><span></span><span></span></div>

<section class="values-band">
  <span class="arrow prev"><svg width="8" height="12" viewBox="0 0 8 12"><path d="M6 1 1 6l5 5" fill="none" stroke="#999" stroke-width="1.3"/></svg></span>
  <h2 class="values-title">WHAT WE VALUE MOST</h2>
  <div class="value-name">E - Enjoy</div>
  <div class="value-line">We will build and maintain an enjoyable work place</div>
  <span class="arrow next"><svg width="8" height="12" viewBox="0 0 8 12"><path d="M2 1l5 5-5 5" fill="none" stroke="#999" stroke-width="1.3"/></svg></span>
</section>

<h2 class="section-title about-title">About Voskin Staffing</h2>
<p class="about-text">Lorem Ipsum is simply dummy text of the printing and typesetting industry. Lorem Ipsum has been the industry's standard dummy text ever since the 1500s, when an unknown printer took a galley of type and scrambled it to make a type specimen book. It has survived not only five centuries, but also the leap into electronic typesetting, remaining essentially unchanged. It was popularised in the 1960s with the release of Letraset sheets containing Lorem Ipsum passages.</p>
<a class="btn-outline" href="#">Read More</a>

<article class="service" style="left:60px">
  <h3>Recruitment</h3>
  <div class="icon"><svg width="34" height="28" viewBox="0 0 34 28"><circle cx="12" cy="8" r="6" fill="#111"/><path d="M1 27c0-8 5-12 11-12s11 4 11 12z" fill="#111"/><circle cx="23" cy="9" r="5" fill="#111"/><path d="M20 15c6 0 12 3 12 12h-7c0-6-2-9-5-12z" fill="#111"/></svg></div>
  <p>Lorem Ipsum is simply dummy text of the printing and typesetting industry</p>
</article>
<article class="service" style="left:239px">
  <h3>Recruitment Process Outsourcing</h3>
  <div class="icon"><svg width="32" height="32" viewBox="0 0 32 32"><g fill="#111"><circle cx="16" cy="16" r="11"/><g id="t"><rect x="13" y="1" width="6" height="7"/><rect x="13" y="24" width="6" height="7"/><rect x="1" y="13" width="7" height="6"/><rect x="24" y="13" width="7" height="6"/></g><use href="#t" transform="rotate(45 16 16)"/></g><circle cx="16" cy="16" r="4.5" fill="#e4e4e4"/></svg></div>
  <p>Lorem Ipsum is simply dummy text of the printing and typesetting industry</p>
</article>
<article class="service" style="left:418px">
  <h3>Talent Management</h3>
  <div class="icon"><svg width="24" height="32" viewBox="0 0 24 32"><path d="M12 2a10 10 0 0 0-6 18c1 1 2 2 2 4h8c0-2 1-3 2-4A10 10 0 0 0 12 2z" fill="none" stroke="#111" stroke-width="2.6"/><rect x="8" y="25" width="8" height="2.5" fill="#111"/><rect x="9" y="29" width="6" height="2.5" fill="#111"/></svg></div>
  <p>Lorem Ipsum is simply dummy text of the printing and typesetting industry</p>
</article>
<article class="service" style="left:597px">
  <h3>Work for Voskin</h3>
  <div class="icon"><svg width="34" height="26" viewBox="0 0 34 26"><path d="M12 5V2h10v3" fill="none" stroke="#111" stroke-width="2.4"/><rect x="1" y="5" width="32" height="20" rx="2" fill="#111"/><rect x="1" y="12" width="32" height="2" fill="#e4e4e4"/><rect x="14" y="10" width="6" height="6" fill="#e4e4e4"/></svg></div>
  <p>Lorem Ipsum is simply dummy text of the printing and typesetting industry</p>
</article>

<h2 class="section-title clients-title">What our Clients Says</h2>
<div class="testimonial-photo" role="img" aria-label="Portrait photo of a smiling client"></div>
<p class="testimonial-text">Lorem Ipsum is simply dummy text of the printing and typesetting industry. Lorem Ipsum has been the industry's standard dummy text ever since the 1500s, when an unknown printer took a galley of type and scrambled it to make a type specimen book. It has survived not only five centuries, but also the leap into electronic typesetting, remaining essentially unchanged. It was popularised in the 1960s with the release of Letraset sheets containing Lorem Ipsum passages.</p>

<footer class="site-footer">
  <a class="brand" href="#">Voskin Staffing</a>
  <nav class="footer-nav">
    <a class="active" href="#">Home</a><a href="#">Our Mission &amp; Vission</a><a href="#">Our Services</a><a href="#">About Us</a><a href="#">Contact Us</a>
  </nav>
</footer>
<div class="footer-base">
  <div class="copyright">© 2014 Voskin Staffing — All Rights Reserved</div>
  <div class="social" aria-label="Social links">
    <span style="background:#3b5998"></span><span style="background:#2aa0d9"></span><span style="background:#d63b2f"></span><span style="background:#1a76b0"></span><span style="background:#2bb5e0"></span>
  </div>
</div>

</body>
</html>
```